Web Design Project

We are looking for a new site design for the KELVO Canada. The current site can be found at
http://www.kelvocanada.example/
The URL is provided for reference. We want a completely different look and layout which is shown in the specifications document.
As part of the design, we want a home page, and inside page.
The design you provide will be implemented in Joomla. The design winner will only need to provide the PSD. We anticipate creating the template coding in-house.
However, if you have experience creating Joomla templates, please let us know as we may ask you to bid separately to do that phase of the project.
We've provided a specifications document which includes wireframes of the home page, and inside page. We've also included a logo file.
For the header at the top, as indicated in the specs document, we want to keep the same overall treatment to every page. We want a graphic treatment with the logo for the header area. In this manner, the design will be flexiable and can be used for future years.
For the home page, we've indicated that we'd like to have a slider implemented within the design.
The wireframe is provided to illustrate the placement of content and menu items. The exact dimensions of each component can be revised as you see fit. We are also flexiable if you feel we have missed items.

```html
<!DOCTYPE html>
<html lang="en">
<head>
<meta charset="utf-8">
<title>KELVO Canada Conference</title>
<link href="https://fonts.googleapis.com/css2?family=PT+Sans:wght@400;700&display=swap" rel="stylesheet">
<style>
:root{
  --brand-blue:#2f4a8a;
  --head-blue:#2c4584;
  --nav-blue:#1d3570;
  --accent-red:#d01010;
  --btn-red:#b80000;
  --panel-grey:#ececec;
  --text:#222;
  --muted:#555;
  --footer:#2b2b2b;
  --white:#fff;
}
*{box-sizing:border-box;margin:0;padding:0}
html,body{width:1200px;height:1200px;overflow:hidden}
body{position:relative;background:var(--white);font-family:Arial,Helvetica,sans-serif;color:var(--text)}
.top-band{position:absolute;left:0;top:0;width:1200px;height:538px;background:var(--brand-blue)}
.header-card{position:absolute;left:102px;top:28px;width:996px;height:510px;background:var(--white);border-radius:10px 10px 0 0}
.abs{position:absolute}
.brand{left:119px;top:42px;display:flex;align-items:center;gap:8px}
.brand-dot{width:18px;height:18px;border-radius:50%;background:var(--brand-blue)}
.brand-name{font-family:"PT Sans",sans-serif;font-weight:700;font-size:28px;color:var(--brand-blue);line-height:1}
.brand-sub{left:147px;top:76px;font-family:"PT Sans",sans-serif;font-weight:700;font-size:11px;letter-spacing:2px;color:var(--brand-blue)}
.utility-nav{right:117px;top:51px;display:flex;font-size:13px;font-weight:700;color:#333}
.utility-nav span{padding:0 12px;border-left:1px solid #ccc;line-height:18px}
.utility-nav span:first-child{border-left:0}
.utility-nav span:last-child{padding-right:0}
.toll{right:116px;top:88px;font-family:"PT Sans",sans-serif;font-size:21px;color:#333}
.toll em{font-style:normal;color:#aaa}
.main-nav{left:273px;top:154px;display:flex;font-size:12px;font-weight:700;color:var(--nav-blue)}
.main-nav span{height:27px;line-height:27px;margin-right:42px}
.main-nav span.active{background:#e4302b;color:var(--white);padding:0 15px;margin-right:28px}
.main-nav span:last-child{margin-right:0}
.nav-rule{left:119px;top:187px;width:962px;height:3px;background:#1a1a1a}
.slider{left:119px;top:191px;width:962px;height:306px;background:linear-gradient(180deg,#e9ecef 0%,#c9ced6 45%,#3b4150 80%,#2a2e38 100%)}
.caption{left:119px;top:459px;width:962px;height:38px;background:rgba(30,30,30,.75)}
.dots{left:137px;top:475px;display:flex;gap:8px}
.dots i{width:8px;height:8px;border-radius:50%;background:var(--white)}
.dots i.on{background:var(--accent-red)}
.caption-text{left:227px;top:463px;font-family:"PT Sans",sans-serif;font-size:24px;color:var(--white)}
.sidebar{left:110px;top:513px;width:227px;height:544px;background:var(--panel-grey);border-radius:4px}
.box-head{position:absolute;height:30px;background:var(--head-blue);border-radius:6px;color:var(--white);font-family:"PT Sans",sans-serif;font-size:20px;line-height:29px;padding-left:9px}
.box-head svg{position:absolute;right:16px;top:12px}
.box-body{position:absolute;background:var(--white);border-radius:5px}
.sponsor{position:absolute;width:60px;height:52px;border-radius:6px;background:#d7dce6}
.field{position:absolute;left:125px;width:190px;height:30px;border:1px solid #ccc;border-radius:6px;font-size:12px;color:#888;padding:8px 4px}
.login-btn{left:126px;top:878px;width:77px;height:24px;background:linear-gradient(#d21010,#9c0000);border-radius:4px;color:var(--white);font-family:"PT Sans",sans-serif;font-weight:700;font-size:15px;text-align:center;line-height:23px}
.social{position:absolute;top:986px;width:37px;height:37px;border-radius:2px}
.welcome-title{left:359px;top:523px;font-family:"PT Sans",sans-serif;font-size:27px;color:#333}
.welcome-copy{left:361px;top:562px;width:506px;font-size:12px;line-height:18px;color:#222}
.welcome-copy p+p{margin-top:18px}
.news{left:879px;top:523px;width:219px;height:284px;background:var(--panel-grey);border-radius:6px}
.news-item{position:absolute;left:888px;width:202px}
.thumb{position:absolute;left:0;top:0;width:42px;height:36px;background:linear-gradient(#d9dde3,#8a8f98);border:2px solid var(--white);box-shadow:0 0 1px #999}
.news-text{position:absolute;left:50px;top:-1px;width:155px;font-size:12px;line-height:14px;color:#555;letter-spacing:.3px}
.news-text b{color:#444}
.news-date{position:absolute;right:0;top:44px;font-size:11px;font-weight:700;color:var(--btn-red);letter-spacing:.5px}
.read-more{left:1014px;top:778px;width:77px;height:20px;background:var(--btn-red);border-radius:4px;color:var(--white);font-size:12px;text-align:center;line-height:20px}
.regions{left:359px;top:834px;width:739px;height:197px;background:var(--panel-grey);border-radius:6px}
.regions-title{left:369px;top:839px;font-family:"PT Sans",sans-serif;font-size:25px;color:#333}
.region{position:absolute;top:880px;width:169px;height:141px;background:var(--white);border-radius:6px;padding:6px 6px 0}
.region h3{font-family:"PT Sans",sans-serif;font-size:17px;color:var(--accent-red);font-weight:700;margin-bottom:5px}
.region li{list-style:none;font-size:12px;font-weight:700;color:#222;padding:5px 2px 5px;border-bottom:1px solid #ddd}
.region li:last-child{border-bottom:0}
.footer{left:0;top:1085px;width:1200px;height:115px;background:var(--footer)}
.footer-links{left:116px;top:1106px;font-size:12px;line-height:24px;color:var(--white)}
.footer-mark{left:980px;top:1125px;display:flex;align-items:center;gap:8px;font-family:"PT Sans",sans-serif;font-weight:700;font-size:24px;color:#9a9a9a}
.footer-mark i{width:16px;height:16px;border-radius:50%;background:#9a9a9a}
</style>
</head>
<body>
<div class="top-band"></div>
<div class="header-card"></div>

<div class="abs brand"><i class="brand-dot"></i><span class="brand-name">KELVO</span></div>
<div class="abs brand-sub">INTERNATIONAL</div>

<nav class="abs utility-nav"><span>Home</span><span>Contact Us</span><span>KELVO International</span></nav>
<div class="abs toll"><em>Toll Free:</em> (123) 456 7890</div>

<nav class="abs main-nav">
  <span class="active">Home</span><span>About</span><span>Board</span><span>Chapters</span><span>Member Space</span><span>Resources &amp; Knowledge</span><span>Sponsorship</span><span>Exhibit</span>
</nav>
<div class="abs nav-rule"></div>

<div class="abs slider" role="img" aria-label="Photo of business people in a meeting around a conference table"></div>
<svg class="abs" style="left:106px;top:332px" width="44" height="56" viewBox="0 0 44 56"><path d="M14 2a26 26 0 0 1 0 52z" fill="#f4f4f4" stroke="#bbb"/><path d="M26 18l-9 10 9 10" fill="none" stroke="#999" stroke-width="4"/></svg>
<svg class="abs" style="left:1050px;top:332px" width="44" height="56" viewBox="0 0 44 56"><path d="M30 2a26 26 0 0 0 0 52z" fill="#f4f4f4" stroke="#bbb"/><path d="M20 18l9 10-9 10" fill="none" stroke="#999" stroke-width="4"/></svg>
<div class="abs caption"></div>
<div class="abs dots"><i></i><i class="on"></i><i></i><i></i><i></i></div>
<div class="abs caption-text">Highlight upcoming conference</div>

<aside class="abs sidebar"></aside>
<div class="box-head" style="left:121px;top:523px;width:201px">Sponsors<svg width="12" height="7"><path d="M0 0h12L6 7z" fill="#fff"/></svg></div>
<div class="box-body" style="left:121px;top:552px;width:201px;height:180px"></div>
<div class="sponsor" style="left:130px;top:582px"></div>
<div class="sponsor" style="left:228px;top:580px;border-radius:50%"></div>
<div class="sponsor" style="left:130px;top:660px"></div>
<div class="sponsor" style="left:222px;top:658px;width:74px"></div>

<div class="box-head" style="left:121px;top:746px;width:201px">Member Login<svg width="12" height="7"><path d="M0 0h12L6 7z" fill="#fff"/></svg></div>
<div class="box-body" style="left:121px;top:776px;width:201px;height:137px"></div>
<div class="field" style="top:796px">Username</div>
<div class="field" style="top:835px">Password</div>
<div class="abs login-btn">Login</div>

<div class="box-head" style="left:121px;top:936px;width:201px">Stay Connected<svg width="12" height="7"><path d="M0 0h12L6 7z" fill="#fff"/></svg></div>
<div class="box-body" style="left:121px;top:966px;width:201px;height:77px"></div>
<div class="social" style="left:127px;background:#f26b1d"></div>
<div class="social" style="left:175px;background:#3b5998"></div>
<div class="social" style="left:224px;background:#c8332a"></div>
<div class="social" style="left:272px;background:#2aa9e0"></div>

<h1 class="abs welcome-title">Welcome to KELVO Canada Conference</h1>
<div class="abs welcome-copy">
  <p>It is a long established fact that a reader will be distracted by the readable content of a page when looking at its layout. The point of using Lorem Ipsum is that it has a more-or-less normal distribution of letters, as opposed to using 'Content here, content here', making it look like readable English.</p>
  <p>Many desktop publishing packages and web page editors now use Lorem Ipsum as their default model text, and a search for 'lorem ipsum' will uncover many web sites still in their infancy.Various versions have evolved over the years, sometimes by accident, sometimes on purpose (injected humour and the like).readable content of a page when looking at its layout. The point of using Lorem Ipsum sometimes on purpose (injected humour and the like).readable content of a page when looking at its layout. The point sometimes on purpose (injected humour and the like).readable content of a page when looking at its layout. The point is that it has a more-or-less normal distribution of letters, as opposed to using 'Content here.</p>
</div>

<section class="abs news"></section>
<div class="box-head" style="left:889px;top:534px;width:195px;height:30px">News and&nbsp; Events</div>
<div class="news-item" style="top:583px"><div class="thumb" role="img" aria-label="Portrait thumbnail"></div><div class="news-text"><b>Lorem Ipsum is simply</b> text of the also a subject matter printing</div><div class="news-date">May 15 , 2012</div></div>
<div class="news-item" style="top:647px"><div class="thumb" role="img" aria-label="Portrait thumbnail"></div><div class="news-text"><b>Lorem Ipsum is simply</b> text of the also a subject matter printing</div><div class="news-date">May 15 , 2012</div></div>
<div class="news-item" style="top:709px"><div class="thumb" role="img" aria-label="Portrait thumbnail"></div><div class="news-text"><b>Lorem Ipsum is simply</b> text of the also a subject matter printing</div><div class="news-date">May 15 , 2012</div></div>
<div class="abs read-more">Read More</div>

<section class="abs regions"></section>
<h2 class="abs regions-title">Regions</h2>
<div class="region" style="left:369px"><h3>Mountain Pacific</h3><ul><li>Vancouver Island</li><li>Vancouver</li><li>Calgary</li></ul></div>
<div class="region" style="left:550px"><h3>Western</h3><ul><li>Edmonton</li><li>Saskatchewan</li><li>Winnipeg</li></ul></div>
<div class="region" style="left:733px;padding-top:3px"><h3>Central</h3><ul><li>National Capital-Ottawa</li><li>Southwestern Ontario</li><li>Montreal</li><li>Toronto</li></ul></div>
<div class="region" style="left:916px"><h3>Atlantic</h3><ul><li>Ova Scotia</li><li>Terra-Nova, St. John's</li><li>Prince Edward Island</li><li>Atlantic, St. John's</li></ul></div>

<footer class="abs footer"></footer>
<div class="abs footer-links">
  Home &nbsp;|&nbsp; About &nbsp;|&nbsp; Board &nbsp;|&nbsp; Chapters &nbsp;|&nbsp; Member Space &nbsp;|&nbsp; Resources &amp; Knowledge &nbsp;|&nbsp; Sponsorship &nbsp;|&nbsp; Exhibit &nbsp;|&nbsp; Member Login &nbsp;|&nbsp; Contact Us<br>
  Privacy Policy &nbsp;|&nbsp; Copyright notice<br>
  Copyright © 2013 northfieldweb. All Rights Reserved.
</div>
<div class="abs footer-mark"><i></i>KELVO</div>
</body>
</html>
```